Business card design needed

Hello, I Need a business card for a company that specialises in providing contract management services for civil construction projects - roads, bridges etc.
I do have a logo that i produced for PLOVER Civilworks however it probably needs a little work, the circles dont have defined edges, i was thinking the colours should reflect the dry interior of Australia progressing out to the colours of the ocean as you move towards the East.... that was my thinking anyway!
Target Market(s)
Professional people generally 30+ yrs old who need professional services to deliver contracts in a high risk environment
Industry/Entity Type
Construction
Contact Information for Business Card
PLOVER Civilworks
Darren Holbeck - Director and Principal Engineer
Registered Professional Engineer of Queensland
Phone 0438 615 272
Email darren@plovercivilworks.com.au
ABN 83 214 570 618
Logo Text
PLOVER Civilworks
Logo styles of interest
Pictorial/Combination Logo
Wordmark Logo
Lettermark Logo
Look and feel

```html
<!DOCTYPE html>
<html lang="en">
<head>
<meta charset="utf-8">
<title>PLOVER Civilworks – Business Card</title>
<link href="https://fonts.googleapis.com/css2?family=Open+Sans:ital,wght@0,400;0,500;0,600;1,400&display=swap" rel="stylesheet">
<style>
  :root {
    --stage: #434343;
    --card: #ffffff;
    --ink: #111111;
    --orange: #ff8000;
    --black: #000000;
    --peach: #fdd6b0;
    --mint: #c4f7b2;
    --sky: #b2d5fb;
    --mark: #ff8000;
  }
  * { margin: 0; padding: 0; box-sizing: border-box; }
  html, body {
    width: 1200px; height: 1000px; overflow: hidden;
    background: var(--stage);
    font-family: "Open Sans", sans-serif;
    color: var(--ink);
  }
  .card {
    position: absolute; left: 68px; top: 193px;
    width: 1063px; height: 613px;
    background: var(--card);
    box-shadow: 4px 6px 8px rgba(0,0,0,0.45);
    overflow: hidden;
  }
  .brand {
    position: absolute; right: 76px; top: 38px;
    display: flex; align-items: center; gap: 22px;
  }
  .brand-dot {
    width: 62px; height: 62px; border-radius: 50%;
    background: var(--mark);
  }
  .brand-name {
    font-size: 64px; font-weight: 500; letter-spacing: -0.5px;
    line-height: 1; color: var(--ink);
  }
  .abn {
    position: absolute; right: 76px; top: 119px;
    font-size: 25px; letter-spacing: 0.5px;
  }
  .hero-art {
    position: absolute; left: 0; top: 212px;
    width: 320px; height: 401px;
    background: linear-gradient(135deg, var(--peach) 0%, var(--mint) 50%, var(--sky) 100%);
  }
  .person { position: absolute; left: 369px; top: 240px; }
  .person-name { font-size: 33px; font-weight: 500; line-height: 1.2; }
  .person-role { margin-top: 12px; font-size: 28.5px; line-height: 1.45; letter-spacing: 0.3px; }
  .person-reg { font-size: 30px; font-style: italic; line-height: 1.4; letter-spacing: 0.2px; }
  .contact {
    position: absolute; left: 369px; top: 426px;
    display: grid; grid-template-columns: 117px auto;
    font-size: 29.5px; line-height: 43px; letter-spacing: 0.2px;
  }
  .contact dt { font-weight: 600; }
  .band-orange {
    position: absolute; left: 0; right: 0; top: 572px; height: 24px;
    background: var(--orange);
  }
  .band-black {
    position: absolute; left: 0; right: 0; top: 599px; height: 14px;
    background: var(--black);
  }
</style>
</head>
<body>
  <div class="card">
    <div class="band-orange"></div>
    <div class="band-black"></div>
    <div class="hero-art" role="img" aria-label="Illustration of a curving road overpass on concrete piers against a pastel backdrop"></div>

    <div class="brand">
      <span class="brand-dot"></span>
      <span class="brand-name">PLOVER Civilworks</span>
    </div>
    <div class="abn">ABN 83 214 570 618</div>

    <div class="person">
      <div class="person-name">Darren Holbeck</div>
      <div class="person-role">Director and Principal Engineer</div>
      <div class="person-reg">Registered Professional Engineer of Queensland</div>
    </div>

    <dl class="contact">
      <dt>Phone</dt><dd>0438 615 272</dd>
      <dt>Email</dt><dd>darren@plovercivilworks.com.au</dd>
    </dl>
  </div>
</body>
</html>
```